Broadcaster,Conference Host,Facilitator

Looking for a business card and logo to create the Grant Ollerby brand .. Something with a slant towards radio and conference speaking
I like the idea of classic black white or grey but open to suggestions

Target Market(s)

Corporates

Industry/Entity Type

Business

Contact Information for Business Card

Grant Ollerby
Email : Grant.Ollerby@fenmail.co.uk
Mobile : +44 7700 384216
Twitter : @Grantollerby

Font styles to use
Serif
Decorative
Script

Requirements
Must have
• Feel classy and dynamic
Should not have
• Cartoons

```html
<!DOCTYPE html>
<html lang="en">
<head>
<meta charset="utf-8">
<title>Grant Ollerby Voice – Business Card</title>
<link rel="stylesheet" href="https://fonts.googleapis.com/css2?family=Jost:wght@300;400&family=Open+Sans:wght@400&display=swap">
<style>
  :root {
    --backdrop: #e8e5e1;
    --card: #000000;
    --ink: #ffffff;
    --rule: #bdbdbd;
  }
  * { margin: 0; padding: 0; box-sizing: border-box; }
  html, body { width: 1200px; height: 1000px; overflow: hidden; }
  body { background: var(--backdrop); position: relative; font-family: "Open Sans", Arial, sans-serif; }

  .card {
    position: absolute;
    left: 266px;
    width: 664px;
    height: 397px;
    background: var(--card);
    border-radius: 24px;
    color: var(--ink);
  }
  .card--upper { top: 73px; }
  .card--lower { top: 533px; }

  .emblem-ring {
    position: absolute;
    left: 264px;
    top: 55px;
    width: 112px;
    height: 112px;
    border: 2px solid var(--ink);
    border-radius: 50%;
  }
  .emblem {
    position: absolute;
    left: 5px;
    top: 5px;
    width: 98px;
    height: 98px;
    border-radius: 50%;
    background: var(--ink);
  }

  .brand-name {
    position: absolute;
    top: 178px;
    left: 0;
    width: 100%;
    text-align: center;
    font-family: "Jost", "Futura", sans-serif;
    font-weight: 300;
    font-size: 42px;
    line-height: 1;
    letter-spacing: 0.5px;
    text-transform: uppercase;
  }
  .brand-tagline {
    position: absolute;
    top: 221px;
    left: 0;
    width: 100%;
    display: flex;
    justify-content: center;
    align-items: center;
    gap: 12px;
    font-family: "Jost", "Futura", sans-serif;
    font-weight: 300;
    font-size: 21px;
    line-height: 1;
    letter-spacing: 6px;
    text-transform: uppercase;
  }
  .brand-tagline .rule {
    width: 76px;
    height: 1px;
    background: var(--rule);
  }

  .contact-icon {
    width: 18px;
    height: 18px;
    display: block;
  }
  .email-icon {
    position: absolute;
    top: 288px;
    left: 323px;
  }
  .email {
    position: absolute;
    top: 309px;
    left: 0;
    width: 100%;
    text-align: center;
    font-size: 16px;
    line-height: 1.2;
  }
  .contact-row {
    position: absolute;
    top: 343px;
    left: 0;
    width: 100%;
    height: 22px;
  }
  .phone {
    position: absolute;
    right: 370px;
    top: 0;
    font-size: 16px;
    line-height: 22px;
  }
  .phone-icon { position: absolute; left: 302px; top: 2px; }
  .divider {
    position: absolute;
    left: 331px;
    top: -2px;
    width: 1px;
    height: 26px;
    background: var(--rule);
  }
  .social-mark {
    position: absolute;
    left: 343px;
    top: 2px;
    width: 18px;
    height: 18px;
    border: 1.5px solid var(--ink);
    border-radius: 50%;
  }
  .handle {
    position: absolute;
    left: 368px;
    top: 0;
    font-size: 16px;
    line-height: 22px;
  }
</style>
</head>
<body>

<div class="card card--upper">
  <div class="emblem-ring"><div class="emblem" role="img" aria-label="Vintage microphone emblem"></div></div>
  <div class="brand-name">Grant Ollerby</div>
  <div class="brand-tagline"><span class="rule"></span><span>Voice</span><span class="rule"></span></div>
  <svg class="contact-icon email-icon" viewBox="0 0 18 18" aria-hidden="true">
    <circle cx="9" cy="9" r="8.2" fill="none" stroke="#fff" stroke-width="1.3"/>
    <rect x="4.5" y="5.8" width="9" height="6.4" fill="#fff"/>
    <path d="M4.5 5.8 L9 9.6 L13.5 5.8" fill="none" stroke="#000" stroke-width="1"/>
  </svg>
  <div class="email">Grant.Ollerby@fenmail.co.uk</div>
  <div class="contact-row">
    <span class="phone">+44 7700 384216</span>
    <svg class="contact-icon phone-icon" viewBox="0 0 18 18" aria-hidden="true">
      <circle cx="9" cy="9" r="8.2" fill="none" stroke="#fff" stroke-width="1.3"/>
      <path d="M4.5 7.5 Q9 4 13.5 7.5 L12.5 9 L11 8.2 L11 7.2 Q9 6.5 7 7.2 L7 8.2 L5.5 9 Z" fill="#fff"/>
      <rect x="5.5" y="9.5" width="7" height="4" rx="1" fill="#fff"/>
    </svg>
    <span class="divider"></span>
    <span class="social-mark"></span>
    <span class="handle">@Grantollerby</span>
  </div>
</div>

<div class="card card--lower">
  <div class="emblem-ring"><div class="emblem" role="img" aria-label="Vintage microphone emblem"></div></div>
  <div class="brand-name">Grant Ollerby</div>
  <div class="brand-tagline"><span class="rule"></span><span>Voice</span><span class="rule"></span></div>
  <svg class="contact-icon email-icon" viewBox="0 0 18 18" aria-hidden="true">
    <circle cx="9" cy="9" r="8.2" fill="none" stroke="#fff" stroke-width="1.3"/>
    <rect x="4.5" y="5.8" width="9" height="6.4" fill="#fff"/>
    <path d="M4.5 5.8 L9 9.6 L13.5 5.8" fill="none" stroke="#000" stroke-width="1"/>
  </svg>
  <div class="email">Grant.Ollerby@fenmail.co.uk</div>
  <div class="contact-row">
    <span class="phone">+44 7700 384216</span>
    <svg class="contact-icon phone-icon" viewBox="0 0 18 18" aria-hidden="true">
      <circle cx="9" cy="9" r="8.2" fill="none" stroke="#fff" stroke-width="1.3"/>
      <path d="M4.5 7.5 Q9 4 13.5 7.5 L12.5 9 L11 8.2 L11 7.2 Q9 6.5 7 7.2 L7 8.2 L5.5 9 Z" fill="#fff"/>
      <rect x="5.5" y="9.5" width="7" height="4" rx="1" fill="#fff"/>
    </svg>
    <span class="divider"></span>
    <span class="social-mark"></span>
    <span class="handle">@Grantollerby</span>
  </div>
</div>

</body>
</html>
```